Info Graphic

We’re looking for a graphic designer to create an infographic that visually communicates Terrafold Collective’s three-phase approach to vegetation management, specifically for high-risk assets like airports. The infographic should effectively tell the story of how our process improves sustainability, reduces costs, and enhances efficiency compared to conventional vegetation management practices.

Project Scope:
Objective:

Develop an engaging and professional infographic that illustrates the three key phases of Terrafold’s approach:
Phase 1 - Audit – Identifying existing vegetation and reviewing current management practices.
Phase 2 Work out a Program – Developing a site-specific plan to address identified issues and meet project KPIs. Matrix of options and budgets
Phase 3 Implementation, Monitoring & Assessment – Full program delivery, stakeholder engagement, project management. Monitor and assess the progress of the program, adjusting strategies as needed, and providing a final report for ongoing management.

Key Requirements:
The infographic should be visually compelling and easy to understand.
It should highlight the benefits of our approach (cost savings, environmental sustainability, efficiency).

The design should align with Terrafold Collective’s branding (colors, typography, style). I can provide some of our other design work so as it remains inline with our current branding options.

I've included the phase detail, an example of something we'd like as well as an example of our PPT.

```html
<!DOCTYPE html>
<html lang="en">
<head>
<meta charset="utf-8">
<title>Terrafold Collective – Three-Phase Approach</title>
<link rel="stylesheet" href="https://fonts.googleapis.com/css2?family=Open+Sans:wght@300;400;700&display=swap">
<style>
  :root {
    --green: #76b82a;
    --ink: #2f2f2f;
    --grey-line: #e3e3e3;
    --hatch: #e6e6e6;
    --paper: #ffffff;
    --brand-grey: #666a6e;
  }
  * { box-sizing: border-box; margin: 0; padding: 0; }
  html, body { width: 1200px; height: 675px; overflow: hidden; background: var(--paper); }
  body { font-family: "Open Sans", Arial, sans-serif; color: var(--ink); }
  .canvas { position: relative; width: 1200px; height: 675px; overflow: hidden; }

  .corner-texture { position: absolute; left: 0; top: 0; width: 330px; height: 146px; }

  .headline {
    position: absolute; left: 136px; top: 54px;
    color: var(--green); font-size: 24px; line-height: 25px; letter-spacing: -0.2px;
  }
  .headline span { display: block; font-weight: 300; }
  .headline .headline-strong { font-weight: 700; }

  .phase-card {
    position: absolute; top: 187px; width: 277px; height: 403px;
    border: 2.5px solid var(--green); border-radius: 9px; background: var(--paper);
  }
  .phase-card::after {
    content: ""; position: absolute; left: 30px; right: 30px; bottom: -14px; height: 14px;
    background: radial-gradient(ellipse at top, rgba(0,0,0,0.22), rgba(0,0,0,0) 70%);
    filter: blur(3px); z-index: -1;
  }
  .phase-1 { left: 134px; }
  .phase-2 { left: 461px; }
  .phase-3 { left: 791px; }

  .phase-title {
    position: absolute; top: 16px; left: 0; right: 0; text-align: center;
    font-size: 29px; font-weight: 400; letter-spacing: 0.5px; color: var(--ink);
  }

  .phase-band {
    position: absolute; left: -2.5px; top: 61px; width: 286px; height: 44px;
  }
  .phase-band svg { position: absolute; inset: 0; }
  .band-label {
    position: absolute; left: 50px; top: 0; height: 44px; line-height: 44px;
    color: #fff; font-weight: 700; font-size: 15px; letter-spacing: 0.2px; white-space: nowrap;
  }
  .phase-3 .band-label { font-size: 14px; left: 49px; }

  .phase-badge {
    position: absolute; left: -21px; top: 54px; width: 57px; height: 57px;
    border-radius: 50%; background: var(--paper); border: 2px solid var(--green);
    display: flex; align-items: center; justify-content: center;
  }
  .badge-icon { width: 32px; height: 32px; border-radius: 50%; background: rgba(118,184,42,0.28); }

  .deliverables { position: absolute; left: 17px; right: 17px; top: 124px; list-style: none; }
  .deliverables li {
    position: relative; height: 32.2px; padding-left: 19px;
    font-size: 15.5px; line-height: 24px; white-space: nowrap; color: var(--ink);
    border-bottom: 1.5px solid var(--grey-line);
    margin-bottom: 0;
  }
  .deliverables li:last-child { border-bottom: none; }
  .deliverables li::before {
    content: ""; position: absolute; left: 2px; top: 8px;
    border-left: 6px solid var(--green); border-top: 5px solid transparent; border-bottom: 5px solid transparent;
  }
  .phase-2 .deliverables li { padding-left: 12px; }
  .phase-2 .deliverables { left: 12px; }
  .phase-3 .deliverables li { padding-left: 16px; }
  .phase-3 .deliverables { left: 19px; }

  .brand-mark {
    position: absolute; right: 38px; top: 606px;
    display: flex; flex-direction: column; align-items: flex-end; gap: 5px;
  }
  .brand-dot { width: 26px; height: 26px; border-radius: 50%; border: 2px solid var(--green); margin-right: 30px; }
  .brand-name { font-size: 12px; font-weight: 400; color: var(--brand-grey); letter-spacing: 0.5px; }

  .footer-bar { position: absolute; left: 0; bottom: 0; width: 1200px; height: 12px; background: var(--green); }
</style>
</head>
<body>
<main class="canvas">
  <svg class="corner-texture" viewBox="0 0 330 146" role="img" aria-label="Fine diagonal line texture in light grey">
    <polygon points="0,0 330,0 233,146 0,146" fill="var(--hatch)"/>
  </svg>

  <h1 class="headline">
    <span>FIND A PROBLEM</span>
    <span class="headline-strong">QUANTIFY THE PROBLEM</span>
    <span>SOLUTION</span>
  </h1>

  <section class="phase-card phase-1">
    <h2 class="phase-title">PHASE 1</h2>
    <div class="phase-band">
      <svg viewBox="0 0 286 44" preserveAspectRatio="none"><polygon points="0,0 279,0 286,22 279,44 0,44" fill="var(--green)"/></svg>
      <span class="band-label">ASSESS + UNDERSTAND</span>
    </div>
    <div class="phase-badge"><div class="badge-icon" role="img" aria-label="Report and magnifier icon"></div></div>
    <ul class="deliverables">
      <li>Site Audit</li>
      <li>Survey &amp; Mapping</li>
      <li>Agronomic Assessment</li>
      <li>Data Analysis</li>
      <li>Issue ID</li>
      <li>Report &amp; Recommendations</li>
      <li>Scorecard</li>
      <li>Risk Identification</li>
    </ul>
  </section>

  <section class="phase-card phase-2">
    <h2 class="phase-title">PHASE 2</h2>
    <div class="phase-band">
      <svg viewBox="0 0 286 44" preserveAspectRatio="none"><polygon points="0,0 279,0 286,22 279,44 0,44" fill="var(--green)"/></svg>
      <span class="band-label">SOLVE</span>
    </div>
    <div class="phase-badge"><div class="badge-icon" role="img" aria-label="Lightbulb with puzzle pieces icon"></div></div>
    <ul class="deliverables">
      <li>Program Options Matrix</li>
      <li>Multiyear Budget Forecast</li>
      <li>Stakeholder Engagement</li>
      <li>ID Guide</li>
      <li>Program Implementation Strategy</li>
      <li>Handbook</li>
      <li>Manual Guide</li>
      <li>Risk Mitigation</li>
    </ul>
  </section>

  <section class="phase-card phase-3">
    <h2 class="phase-title">PHASE 3</h2>
    <div class="phase-band">
      <svg viewBox="0 0 286 44" preserveAspectRatio="none"><polygon points="0,0 286,0 286,44 0,44" fill="var(--green)"/></svg>
      <span class="band-label">GUIDE - MONITOR - EVALUATE</span>
    </div>
    <div class="phase-badge"><div class="badge-icon" role="img" aria-label="Lightbulb and gear cycle icon"></div></div>
    <ul class="deliverables">
      <li>Full Program</li>
      <li>Detailed Implementation Plan</li>
      <li>Training</li>
      <li>Stakeholder Management</li>
      <li>Project Management</li>
      <li>Delivery Support</li>
      <li>Scientific Monitoring</li>
      <li>Reporting</li>
    </ul>
  </section>

  <div class="brand-mark">
    <span class="brand-dot"></span>
    <span class="brand-name">Terrafold Collective</span>
  </div>

  <div class="footer-bar"></div>
</main>
</body>
</html>
```